poster design for a sales competition

we are requiring a series of posters for sales competitions. The posters should reflect that it is a race and there is a winner, so the poster imagery will motivate the sales team to sell more,
the posters will require blank fields for names of the contestants and space for progressive scores/tally
suggestions: racetrack ie horse/car/track and field etc.or a graph or anything that has a start and finish
eg if it is a race maybe stands around the border of the track.
the blank fields will accomodate 10-12 contestants and as such will need their own lanes that can be filled in as they progress over the sales competition period,another idea is perhaps at the bottom of the poster you could have a series of cutouts eg car race theme colour coded race cars that once cut out could be blue tacked to the poster to create a 2D image and competition position around the track./

we are requiring several different themes and designs and will offer 2nd and 3rd place payments and more if we recieve a number of satisfactory designs

Target Market(s)

the audience is highly motivated sales peoplefrom your design and others i know my concept is difficult to get so i'll try and explain the poster is a race between sales persons(SP) if you have a 10 week sales contest and 8 (SP) the first week one (SP) sells $5000 and one sells $4000 one sells $2000 etc the one who sells most will be the leader in the pool each week they will progress up the pool over the 10 weeks until the end and the winner is the leader, the poster is avisual of their performance against the other (SP)

Industry/Entity Type

Progressive

Requirements
Must have
• start and finish
blank fields for weekly/daily sales results
blank fields for the sales teams names
size is A1 or A0
images to be free of copyright
Nice to have
• should have a theme
can have cut outs
can have space for competition start and finish dates

```html
<!DOCTYPE html>
<html lang="en">
<head>
<meta charset="utf-8">
<title>Sales Race Pool Poster</title>
<link href="https://fonts.googleapis.com/css2?family=Ultra&family=Libre+Baskerville:wght@700&display=swap" rel="stylesheet">
<style>
  :root {
    --pink: #f4a9b2;
    --pink-line: rgba(255,255,255,0.35);
    --water: #aee1ed;
    --lane-blue: #6f7fc4;
    --rope-red: #e0141c;
    --rope-white: #ffffff;
    --block-dark: #8a8a8a;
    --block-light: #f2f2f2;
    --ink: #111111;
    --paper: #ffffff;
    --cutout-fill: #eef1f4;
  }
  html, body {
    margin: 0;
    padding: 0;
    overflow: hidden;
  }
  .poster {
    position: relative;
    width: 855px;
    height: 1200px;
    overflow: hidden;
    background:
      repeating-linear-gradient(to bottom, var(--pink) 0 3px, var(--pink-line) 3px 4px),
      var(--pink);
  }
  .finish-title {
    position: absolute;
    top: 8px;
    left: 72px;
    width: 768px;
    margin: 0;
    text-align: center;
    font-family: "Ultra", serif;
    font-size: 58px;
    line-height: 66px;
    letter-spacing: 4px;
    color: var(--ink);
  }
  .pool {
    position: absolute;
    left: 72px;
    top: 84px;
    width: 768px;
    height: 771px;
    background: var(--water);
  }
  .lane-line {
    position: absolute;
    top: 14px;
    width: 5px;
    height: 700px;
    margin-left: -2.5px;
    background: var(--lane-blue);
  }
  .lane-rope {
    position: absolute;
    top: 14px;
    width: 6px;
    height: 740px;
    margin-left: -3px;
    background: repeating-linear-gradient(to bottom,
      var(--rope-white) 0px,
      var(--rope-red) 36px,
      var(--rope-red) 44px,
      var(--rope-white) 80px,
      var(--rope-white) 145px);
  }
  .start-block {
    position: absolute;
    top: 639px;
    width: 82px;
    height: 125px;
    margin-left: -41px;
    background: linear-gradient(to right, var(--block-dark), var(--block-light) 50%, var(--block-dark));
    border-top: 8px solid var(--block-light);
    box-sizing: border-box;
  }
  .week-marker {
    position: absolute;
    left: 12px;
    font-family: "Libre Baskerville", serif;
    font-weight: 700;
    font-size: 13px;
    color: var(--ink);
  }
  .name-hint {
    position: absolute;
    top: 893px;
    font-family: "Libre Baskerville", serif;
    font-size: 6px;
    color: #555;
  }
  .cutout-sheet {
    position: absolute;
    left: 0;
    top: 911px;
    width: 855px;
    height: 289px;
    background: var(--paper);
  }
  .cutout-row {
    position: absolute;
    left: 0;
    width: 855px;
    height: 52px;
  }
  .cutout-label {
    position: absolute;
    left: 12px;
    top: 16px;
    font-family: "Libre Baskerville", serif;
    font-weight: 700;
    font-size: 13px;
    color: var(--ink);
  }
  .cutout-figures {
    position: absolute;
    left: 108px;
    top: 0;
    width: 737px;
    height: 52px;
    background: var(--cutout-fill);
  }
</style>
</head>
<body>
<main class="poster">
  <h1 class="finish-title">FINISH</h1>

  <section class="pool">
    <div class="lane-rope" style="left:0"></div>
    <div class="lane-rope" style="left:96px"></div>
    <div class="lane-rope" style="left:192px"></div>
    <div class="lane-rope" style="left:288px"></div>
    <div class="lane-rope" style="left:384px"></div>
    <div class="lane-rope" style="left:480px"></div>
    <div class="lane-rope" style="left:576px"></div>
    <div class="lane-rope" style="left:672px"></div>
    <div class="lane-rope" style="left:768px"></div>

    <div class="lane-line" style="left:48px"></div>
    <div class="lane-line" style="left:144px"></div>
    <div class="lane-line" style="left:240px"></div>
    <div class="lane-line" style="left:336px"></div>
    <div class="lane-line" style="left:432px"></div>
    <div class="lane-line" style="left:528px"></div>
    <div class="lane-line" style="left:624px"></div>
    <div class="lane-line" style="left:720px"></div>

    <div class="start-block" style="left:48px"></div>
    <div class="start-block" style="left:144px"></div>
    <div class="start-block" style="left:240px"></div>
    <div class="start-block" style="left:336px"></div>
    <div class="start-block" style="left:432px"></div>
    <div class="start-block" style="left:528px"></div>
    <div class="start-block" style="left:624px"></div>
    <div class="start-block" style="left:720px"></div>
  </section>

  <div class="week-marker" style="top:203px">Week 4</div>
  <div class="week-marker" style="top:340px">Week 3</div>
  <div class="week-marker" style="top:474px">Week 2</div>
  <div class="week-marker" style="top:625px">Week 1</div>

  <div class="name-hint" style="left:80px">Name</div>
  <div class="name-hint" style="left:282px">Name</div>
  <div class="name-hint" style="left:535px">Name</div>

  <section class="cutout-sheet">
    <div class="cutout-row" style="top:16px">
      <span class="cutout-label">Week1</span>
      <div class="cutout-figures" role="img" aria-label="Eight outlined fish cut-outs for week 1"></div>
    </div>
    <div class="cutout-row" style="top:72px">
      <span class="cutout-label">week 2</span>
      <div class="cutout-figures" role="img" aria-label="Eight outlined fish cut-outs for week 2"></div>
    </div>
    <div class="cutout-row" style="top:132px">
      <span class="cutout-label">week 3</span>
      <div class="cutout-figures" role="img" aria-label="Eight outlined fish cut-outs for week 3"></div>
    </div>
    <div class="cutout-row" style="top:190px">
      <span class="cutout-label">Week 4</span>
      <div class="cutout-figures" role="img" aria-label="Eight outlined fish cut-outs for week 4"></div>
    </div>
  </section>
</main>
</body>
</html>
```